High End Notary Service Business Card Design

Want a professional and elegant/luxurious business card that is clean and simple in the design. A notary is a trusted professional that helps people sign very important documents. The card should be in alignment with this service provided.

Most of the time, service will be for the purchase of a home or refinance of a mortgage

There is NO LOGO. This is aesthetic. A look and feel. Conveying professionalism and concierge level of service.

Target Market(s)

Other business professionals, Lawyers, Escrow Officers, Loan Officers

Industry/Entity Type

Legal

Contact Information for Business Card

This will be a one-sided business card

Colors
35a7d7
3176b5
85cae6
d3a5cc
b868aa
ffffff
0356a4

Requirements
Must have
• Lorena T. Mirabel-Hodgkins
Notary Public

642-871-3094
MirabelSigningDesk@Wexmail.com
Nice to have
• Headshot photo below. Convey the aspect of signing documents. No black cards. Preference is shades of blue: light blue, navy, aqua, gold, white, or lavendar, etc.
Should not have
• No scales or legal scales.

```html
<!DOCTYPE html>
<html lang="en">
<head>
<meta charset="utf-8">
<title>Lorena T. Mirabel-Hodgkins – Notary Public Card</title>
<link href="https://fonts.googleapis.com/css2?family=Jost:wght@400;500&display=swap" rel="stylesheet">
<style>
  :root {
    --backdrop: #cccccc;
    --card: #ffffff;
    --navy: #0356a4;
    --ink: #333333;
    --photo-light: #a9a9a9;
    --photo-dark: #5e5e5e;
  }
  * { margin: 0; padding: 0; box-sizing: border-box; }
  html, body {
    width: 1200px;
    height: 900px;
    overflow: hidden;
    background: var(--backdrop);
    font-family: "Jost", "Futura", sans-serif;
  }
  .canvas {
    position: relative;
    width: 1200px;
    height: 900px;
  }
  .business-card {
    position: absolute;
    left: 355px;
    top: 22px;
    width: 490px;
    height: 856px;
    background: var(--card);
    border-radius: 30px;
    text-align: center;
  }
  .headshot {
    position: absolute;
    left: 70px;
    top: 87px;
    width: 348px;
    height: 348px;
    border-radius: 50%;
    background: radial-gradient(circle at 50% 45%, var(--photo-light) 0%, #8c8c8c 55%, var(--photo-dark) 100%);
  }
  .identity {
    position: absolute;
    left: 0;
    right: 0;
    top: 596px;
  }
  .name {
    color: var(--navy);
    font-size: 25px;
    font-weight: 400;
    letter-spacing: 0.3px;
    line-height: 1.2;
  }
  .title {
    color: var(--ink);
    font-size: 20px;
    letter-spacing: 0.6px;
    line-height: 1.2;
    margin-top: 2px;
  }
  .contact-icons {
    position: absolute;
    left: 0;
    right: 0;
    top: 673px;
    display: flex;
    justify-content: center;
    gap: 11px;
  }
  .contact-icons svg { width: 26px; height: 26px; }
  .contact-lines {
    position: absolute;
    left: 0;
    right: 0;
    top: 716px;
    color: var(--ink);
    font-size: 20px;
    letter-spacing: 0.6px;
    line-height: 30px;
  }
</style>
</head>
<body>
<div class="canvas">
  <div class="business-card">
    <div class="headshot" role="img" aria-label="Black and white circular headshot portrait of the notary"></div>

    <div class="identity">
      <h1 class="name">LORENA T. MIRABEL-HODGKINS</h1>
      <p class="title">Notary Public</p>
    </div>

    <div class="contact-icons">
      <svg viewBox="0 0 26 26" aria-label="Phone">
        <circle cx="13" cy="13" r="12" fill="none" stroke="var(--navy)" stroke-width="1.5"/>
        <path d="M9.5 7.5c.6-.5 1.4-.4 1.8.2l1 1.6c.3.5.2 1.1-.2 1.5l-.8.7c.6 1.6 1.5 2.9 2.8 4l.9-.6c.5-.3 1.1-.3 1.5.1l1.3 1.3c.5.5.5 1.3-.1 1.8l-.8.7c-.8.6-2 .7-2.9.1-2.9-1.9-5-4.9-5.7-8.2-.2-1 .2-2 1-2.7z" fill="none" stroke="var(--navy)" stroke-width="1.3" stroke-linejoin="round"/>
      </svg>
      <svg viewBox="0 0 26 26" aria-label="Email">
        <circle cx="13" cy="13" r="12" fill="none" stroke="var(--navy)" stroke-width="1.5"/>
        <rect x="7.5" y="9" width="11" height="8" rx="1" fill="none" stroke="var(--navy)" stroke-width="1.3"/>
        <path d="M7.8 9.4L13 13.5l5.2-4.1" fill="none" stroke="var(--navy)" stroke-width="1.3" stroke-linejoin="round"/>
      </svg>
    </div>

    <div class="contact-lines">
      <p class="phone">642-871-3094</p>
      <p class="email">MirabelSigningDesk@Wexmail.com</p>
    </div>
  </div>
</div>
</body>
</html>
```